Maren's Treasured Tunes - 2014

I need a CD cover and insert design for a CD that includes songs my daughter (Maren Dulack) has recorded. She is a 17 year old vocalist and uses accompaniment tracks as well as 2 songs with live accompaniment. The CD is dedicated to her mother and each song is dedicated to an individual. The CD is intended to be given as gifts to family and friends.

The CD is titled "2014"

There are 5 songs on the CD:

1. "Evening Lantern" (originally recorded by Paolo Vantreni and Lorette Fave). This is a duet with Maren and her father.
2. "Open Road" (Originally recorded by Copper Hollows). This is a duet Maren and her father.
3. "All That Your Mercy Holds" (originally recorded by Gloria Bastrelli) This is sung by Maren. Accompanied on keyboard by Tamsin Holgreve.
4. "Keep a Light On For Me" (originally sung by Vera Castlewood).
5. "Lean On Us" (originally sung by Dario Quell) sung by Maren accompanied on guitar by Tamsin Holgreve.

This is a mixture of songs that have special meaning to Maren. The CD should convey her fun, bubbly but mature personality. It should be colorful and fun not dark and harsh. She is a "Texas" girl but she isn't into country music. She loves anything "Texas".

With the dedications included for each song and the CD, there will need to be interior printing and background design that may include a foldout in order to fit everything.

CD Dedication:
"I dedicate this cd to my mom. Even though I don't show it all the time, I appreciate her and the unconditional love she shows me. Through everything that I do I want to make her proud. Thank you for always having hope and faith in me and providing a life for me that I am so blessed to live. I love you more an more every day"

Song Dedications:
"Evening Lantern"
As many people know, “Evening Lantern” has been our most requested song to sing. Growing up I had heard my dad sing this song with my aunt and I was so mesmerized by their performances and couldn’t wait to one day sing this song with my dad. My dad and I have been singing together since I was 4 but this song sparked a different kind of relationship and musical connection with him. It was challenging at first and he pushed me to work hard and to push myself to discover vocal capabilities that I didn’t know I had. I dedicate this song to my dad for always motivating me to be the best I can be not only musically but socially, academically and most of all spiritually. Dad, I love you more than words can say.

"Open Road"
I have never been a fan of country music let alone attempted to sing a country song but this song completely changed my perspective on it. My dad and I first sang this song at our Pastors retirement party celebrating he and his wife’s 23 year long dedication to our church and to recognize his love for country music. They became apart of our family in many ways and I am so blessed to call them family. This song is dedicated to Pastor Glen and Faye Durbin for everything fron putting up with my grandparents to sharing every Easter with us. I miss them so much but I know that they will forever be apart of our family no matter where God places them.

"All That Your Mercy Holds"
When first introduced to this song I hated it. When having to choose a song to sing I always went with a ballad because that was my comfort zone. So when asked to sing a gospel song I was very overwhelmed. I never fully understood why people would say that they are “in love with music” or “music was their passion”. I obviously enjoyed music but I had never felt that connection with it until the first time I performed this song. Every note, every word, every dynamic meant something to me and my passion for music was forever changed. I dedicate this song to Tamsin Holgreve for working with me hour upon hour to help me vocally improve and for teaching me that it’s okay to step outside the box and to not just be comfortable all the time.

"Keep a Light on for Me"
I heard this song for the first time and sang it 3 days later for my end of the year choir concert. My mom had been searching songs for me to sing and as soon as she introduced this song to me I fell in love with it. This song is typically meant to be sung about a romantic love but while performing this song I couldn’t help but think of my grandparents and how they are always watching over me. I dedicate this song to my guardian angels, my protectors, and the two people that I love and miss more than anything in this world Oma and Opa.

"Lean On Us"
When I first sang this song I was performing at my voice recital for school. I chose to sing this song because it was fun and sweet. In the past few months this song has become very real to me. Although God and family are top priorities in my life, friends are such a huge part of my life as well. In 6Th grade I started a friendship with someone that I never knew would make such a great impact on my life. She became someone that I looked up to and someone that I could truly call my best friend. I dedicate this song to Kaylee Brandt for always putting up with me and investing in not only my life but my family’s life. No matter where life takes us in the next year I will forever be thankful for her friendship.

Special thanks to:

My Momma
Marla Quince (voice coach)
Lulu Padgett (High School choir director)
Mark Ostrand
Grant Vossler (Producer)

IMG_9670 is for the cover and IMG_9672 is for the back.

Thanks,

Curtis Dulack (father)

```html
<!DOCTYPE html>
<html lang="en">
<head>
<meta charset="utf-8">
<title>Maren's Treasured Tunes - 2014</title>
<link href="https://fonts.googleapis.com/css2?family=Pinyon+Script&family=Sofia&display=swap" rel="stylesheet">
<style>
  :root {
    --ink: #3a3130;
    --ink-soft: #4a403c;
    --white: #ffffff;
    --brick-pale: #efd6c8;
    --garden-pale: #dfe8d0;
    --path-pale: #e9e2da;
    --leaf-deep: #1f2a14;
    --leaf-mid: #3d4a26;
    --bark: #4a3a2a;
    --dress-coral: #e0675f;
  }
  * { margin: 0; padding: 0; box-sizing: border-box; }
  html, body { width: 1200px; height: 600px; overflow: hidden; background: var(--white); }
  .spread { position: relative; width: 1200px; height: 600px; display: flex; }

  .back-panel { position: relative; width: 600px; height: 600px; overflow: hidden; }
  .back-photo {
    position: absolute; inset: 0;
    background:
      linear-gradient(90deg, var(--brick-pale) 0 17%, transparent 17% 76%, var(--brick-pale) 76% 100%),
      linear-gradient(180deg, var(--garden-pale) 0%, #e8eedc 55%, var(--path-pale) 75%, #eadcd2 100%);
  }
  .tracklist {
    position: absolute; left: 73px; top: 150px; width: 470px;
    list-style: none; font-family: "Sofia", cursive; color: var(--ink);
  }
  .track { margin-bottom: 10px; }
  .track-title { font-size: 25px; line-height: 30px; color: var(--ink); }
  .track-note { font-size: 15px; line-height: 21px; color: var(--ink-soft); }

  .cover-panel { position: relative; width: 600px; height: 600px; overflow: hidden; }
  .cover-photo {
    position: absolute; inset: 0;
    background:
      linear-gradient(90deg, transparent 0 64%, var(--bark) 70%, #5a4734 100%),
      radial-gradient(ellipse 35% 40% at 50% 100%, var(--dress-coral) 0%, transparent 100%),
      radial-gradient(ellipse 30% 35% at 45% 45%, #a0745c 0%, transparent 100%),
      linear-gradient(160deg, var(--leaf-mid) 0%, var(--leaf-deep) 60%, #2b2418 100%);
  }
  .cover-year {
    position: absolute; left: 38px; top: 22px;
    font-family: "Pinyon Script", cursive; font-size: 58px; color: var(--white);
  }
  .cover-name {
    position: absolute; right: 46px; top: 500px;
    font-family: "Pinyon Script", cursive; font-size: 34px; color: var(--white);
  }
</style>
</head>
<body>
<main class="spread">
  <section class="back-panel">
    <div class="back-photo" role="img" aria-label="Soft, faded portrait of Maren standing between two brick pillars in a garden, wearing a coral top, white skirt and boots"></div>
    <ol class="tracklist">
      <li class="track">
        <p class="track-title">1. "Evening Lantern"</p>
        <p class="track-note">(Originally recorded by Paolo Vantreni and Lorette Fave). This is a duet with Maren and her father.</p>
      </li>
      <li class="track">
        <p class="track-title">2. "Open Road"</p>
        <p class="track-note">(Originally recorded by Copper Hollows). This is a duet Maren and her father.</p>
      </li>
      <li class="track">
        <p class="track-title">3. "All That Your Mercy Holds"</p>
        <p class="track-note">(Originally recorded by Gloria Bastrelli) This is sung by Maren. Accompanied on keyboard by Tamsin Holgreve.</p>
      </li>
      <li class="track">
        <p class="track-title">4. "Keep a Light On For Me"</p>
        <p class="track-note">(Originally sung by Vera Castlewood).</p>
      </li>
      <li class="track">
        <p class="track-title">5. "Lean On Us"</p>
        <p class="track-note">(Originally sung by Dario Quell) sung by Maren accompanied on guitar by Tamsin Holgreve.</p>
      </li>
    </ol>
  </section>

  <section class="cover-panel">
    <div class="cover-photo" role="img" aria-label="Portrait of Maren in a coral lace top leaning against a tree trunk, with soft green foliage behind"></div>
    <h1 class="cover-year">2014</h1>
    <p class="cover-name">Maren Dulack</p>
  </section>
</main>
</body>
</html>
```